PowerPoint Template - Multiple Slide Backgrounds

Looking for a professional PowerPoint template for a technology company. You will see with the logo there's sort of a theme with gears and a lightbulb of sorts. Keeping with this sort of design could help with the brand.

Branding information
• Logo with transparent background included
• Primary Color (Orange) Hex #E6753D
• Secondary Color (Brown) Hex #6A4238
• Primary Font - Myriad Pro
• Secondary Font - Quiet Sans Light

Design request -
• PowerPoint (POTX) template with master slide views
• Cover Slide
• Color Pallet - 7 Color PowerPoint pallet that includes and complements primary and secondary colors
• Slide Master with Footer
• Multiple Background Types to allow for smart art overlay or bullet point text boxes
Bonus - Sample graphical elements using shapes and smart art

```html
<!DOCTYPE html>
<html lang="en">
<head>
<meta charset="utf-8">
<title>Brightgear Labs – Presentation Template</title>
<link href="https://fonts.googleapis.com/css2?family=Source+Sans+3:wght@300;400;600;700&display=swap" rel="stylesheet">
<style>
:root{
  --orange:#E6753D;
  --orange-light:#F0996A;
  --orange-deep:#C85E2A;
  --brown:#6A4238;
  --brown-dark:#4E2F27;
  --ink:#4A3630;
  --text-grey:#8A8A8A;
  --rule:#D9D9D9;
  --band:#EFEFEF;
  --row:#F1F1F1;
  --white:#FFFFFF;
  --canvas:#000000;
}
*{box-sizing:border-box;margin:0;padding:0}
html,body{width:1180px;height:1200px;overflow:hidden;background:var(--canvas)}
.canvas{position:relative;width:1180px;height:1200px;overflow:hidden;background:var(--canvas);font-family:'Source Sans 3',sans-serif}

/* slide frame: every slide is designed at 592 × 320 */
.slide{position:absolute;width:592px;height:320px;overflow:hidden;background:var(--white);font-family:'Source Sans 3',sans-serif}
.slide--thumb{transform:scale(.4257);transform-origin:0 0}

/* shared pieces */
.rule{position:absolute;left:30px;top:0;bottom:0;width:1px;background:var(--rule)}
.rule--light{background:rgba(255,255,255,.45)}
.bar{position:absolute;left:28px;width:5px;background:var(--orange)}
.bar--brown{background:var(--brown)}
.bar--white{background:var(--white)}
.head{position:absolute;left:44px;top:36px}
.sub{color:var(--orange);font-size:15px;line-height:17px;font-weight:400}
.ttl{color:var(--ink);font-size:19px;line-height:21px;font-weight:700}
.head--light .sub,.head--light .ttl{color:var(--white)}
.copy{color:var(--text-grey);font-size:10px;line-height:15.4px}
.copy p+p{margin-top:15px}
.copy--light{color:rgba(255,255,255,.88)}
.footer{position:absolute;left:0;right:0;bottom:0;height:18px;background:var(--band);font-size:8.5px;line-height:18px;color:#555;padding-left:9px}
.footer--clear{background:transparent;color:rgba(255,255,255,.8)}
.page{position:absolute;right:8px;bottom:4px;width:22px;height:22px;border-radius:50%;background:var(--orange);color:var(--white);font-size:9px;font-weight:700;text-align:center;line-height:22px}
.mark{position:absolute;top:14px;right:12px;display:flex;align-items:center;gap:4px;font-size:10px;font-weight:700;color:var(--brown)}
.mark-dot{width:9px;height:9px;border-radius:50%;background:var(--orange)}
.mark--light{color:var(--white)}
.mark--light .mark-dot{background:var(--white)}

/* brand lockup */
.lockup{position:absolute;transform:translate(-50%,-50%)}
.lockup-row{display:flex;align-items:center;justify-content:center;gap:6px}
.lockup-dot{width:12px;height:12px;border-radius:50%;background:var(--orange);flex:none}
.lockup-name{font-size:19px;font-weight:700;color:var(--brown);line-height:1;white-space:nowrap}

/* placeholder fills */
.fill{position:absolute}
.fill--blueprint{inset:0;background:radial-gradient(circle at 35% 55%,#EC8A55 0%,var(--orange) 45%,#E06F37 100%)}
.fill--gears-warm{background:linear-gradient(135deg,#D9733F 0%,var(--orange) 45%,#C9622E 100%)}
.fill--gears-glow{background:linear-gradient(90deg,#5A3428 0%,#8C4A2C 45%,#E08A55 75%,#6A3A2A 100%)}
.fill--hand-gears{background:linear-gradient(120deg,#F6E3D3 0%,#E9B48E 50%,#F3DCCA 100%)}

/* cover-type slides */
.panel-brown{position:absolute;left:0;top:0;bottom:0;width:396px;background:var(--brown)}
.edge-brown{position:absolute;right:0;top:0;bottom:0;width:13px;background:var(--brown)}
.panel-orange{position:absolute;left:0;top:0;bottom:0;width:365px;background:var(--orange)}
.display{position:absolute;color:var(--white);font-weight:700;font-size:26px;line-height:30px}
.display-sub{font-weight:400;font-size:17px;line-height:20px}

/* contact */
.contact{position:absolute;left:56px;top:68px;color:var(--white)}
.contact h2{font-size:24px;font-weight:600;line-height:28px;margin-bottom:14px}
.contact p{font-size:15px;line-height:21px}
.contact p+p{margin-top:14px}

/* icon features */
.features{position:absolute;left:20px;right:20px;display:flex;justify-content:space-between}
.feature{width:168px;text-align:center}
.feature svg{width:38px;height:38px;display:block;margin:0 auto 4px}
.feature h3{font-size:9.5px;font-weight:700;line-height:12px;margin-bottom:3px}
.feature p{font-size:8px;line-height:12.6px}
.features--light{color:var(--white)}
.features--light svg{fill:var(--white)}
.features--dark h3{color:var(--orange)}
.features--dark p{color:var(--text-grey)}
.features--dark svg{fill:var(--orange)}

/* table */
.data-table{position:absolute;left:15px;top:68px;width:571px;border-collapse:collapse;font-size:8.5px}
.data-table th{background:var(--orange);color:var(--white);text-align:left;font-weight:700;height:22px;padding:0 12px}
.data-table td{height:41px;padding:0 12px;color:var(--ink);vertical-align:middle}
.data-table td.label{width:115px;font-weight:600;color:var(--brown)}
.data-table td.desc{color:var(--text-grey);font-size:7.6px;line-height:11px}
.data-table tr:nth-child(odd) td{background:var(--row)}

.chart{position:absolute;left:0;top:0}
</style>
</head>
<body>
<svg width="0" height="0" style="position:absolute" aria-hidden="true">
  <symbol id="icon-phone" viewBox="0 0 24 24"><path d="M7 1h10a2 2 0 0 1 2 2v18a2 2 0 0 1-2 2H7a2 2 0 0 1-2-2V3a2 2 0 0 1 2-2zm0 3v14h10V4H7zm5 15.5a1.2 1.2 0 1 0 0 2.4 1.2 1.2 0 0 0 0-2.4z"/></symbol>
  <symbol id="icon-team" viewBox="0 0 24 24"><circle cx="12" cy="6" r="3.2"/><circle cx="5.5" cy="8.5" r="2.4"/><circle cx="18.5" cy="8.5" r="2.4"/><path d="M6.5 21v-5a5.5 5.5 0 0 1 11 0v5z"/><path d="M1 21v-3.5a4 4 0 0 1 5-3.9V21zM23 21v-3.5a4 4 0 0 0-5-3.9V21z"/></symbol>
  <symbol id="icon-chart" viewBox="0 0 24 24"><path d="M2 21h20v1.5H2zM4 14h3v6H4zM9 10h3v10H9zM14 7h3v13h-3zM19 3h3v17h-3z"/></symbol>
</svg>

<main class="canvas">

  <!-- ========== large previews ========== -->
  <section class="slide slide--closing" style="left:22px;top:8px">
    <div class="panel-brown"></div>
    <div class="edge-brown"></div>
    <div class="rule rule--light" style="left:39px"></div>
    <div class="bar" style="left:37px;top:132px;height:52px"></div>
    <h1 class="display" style="left:52px;top:143px">Thank you for your time</h1>
    <div class="lockup" style="left:488px;top:190px">
      <div class="lockup-row"><span class="lockup-dot"></span><span class="lockup-name">Brightgear Labs</span></div>
    </div>
  </section>

  <section class="slide slide--divider" style="left:22px;top:376px">
    <div class="fill fill--blueprint" role="img" aria-label="Faint blueprint drawing of gears and machine parts"></div>
    <div class="rule rule--light" style="left:39px;bottom:108px"></div>
    <div class="bar bar--brown" style="left:37px;top:130px;height:62px"></div>
    <h1 class="display" style="left:53px;top:134px;font-size:24px">Sectione Divider Title Here<br><span class="display-sub">Subtitle Here</span></h1>
    <div class="mark mark--light"><span class="mark-dot"></span>Brightgear</div>
  </section>

  <section class="slide slide--paragraph" style="left:22px;top:730px">
    <div class="rule"></div>
    <div class="bar" style="top:34px;height:40px"></div>
    <div class="head"><p class="sub">Subtitle Here</p><h2 class="ttl">Paragraph Title</h2></div>
    <div class="mark"><span class="mark-dot"></span>Brightgear</div>
    <div class="copy" style="position:absolute;left:45px;width:518px;top:79px">
      <p>Lorem Ipsum is simply dummy text of the printing and typesetting industry. Lorem Ipsum has been the industry's standard dummy text ever since the 1500s, when an unknown printer took a galley of type and scrambled it to make a type specimen book. It has survived not only five centuries, but also the leap into electronic typesetting, remaining essentially unchanged. It was popularised in the 1960s with the release of Dryset sheets containing Lorem Ipsum passages, and more recently with desktop publishing software like Folio Pagesmith including versions of Lorem Ipsum. Lorem Ipsum is simply dummy text of the printing and typesetting industry.</p>
      <p>Lorem Ipsum has been the industry's standard dummy text ever since the 1500s, when an unknown printer took a galley of type and scrambled it to make a type specimen book. It has survived not only five centuries, but also the leap into electronic typesetting, remaining essentially unchanged.</p>
      <p>It was popularised in the 1960s with the release of Dryset sheets containing Lorem Ipsum passages, and more recently with desktop publishing software like Folio Pagesmith including versions of Lorem Ipsum.</p>
    </div>
    <div class="footer">Copyright text here</div>
    <div class="page">01</div>
  </section>

  <section class="slide slide--two-column" style="left:22px;top:1070px">
    <div class="rule"></div>
    <div class="bar" style="top:34px;height:40px"></div>
    <div class="head"><p class="sub">Subtitle Here</p><h2 class="ttl">Paragraph Title</h2></div>
    <div class="mark"><span class="mark-dot"></span>Brightgear</div>
    <div class="copy" style="position:absolute;left:45px;width:245px;top:79px">Lorem Ipsum is simply dummy text of the printing and typesetting industry. Lorem Ipsum has been the industry's standard dummy text ever since the 1500s, when an unknown printer took a galley of type and scrambled it to make a type specimen book.</div>
    <div class="copy" style="position:absolute;left:317px;width:245px;top:79px">Lorem Ipsum is simply dummy text of the printing and typesetting industry. Lorem Ipsum has been the industry's standard dummy text ever since the 1500s, when an unknown printer took a galley of type and scrambled it to make a type specimen book.</div>
  </section>

  <!-- ========== thumbnails, column A ========== -->
  <section class="slide slide--thumb slide--contact" style="left:653px;top:8px">
    <div class="panel-orange"></div>
    <div class="rule rule--light" style="left:39px"></div>
    <div class="bar bar--white" style="left:37px;top:64px;height:34px"></div>
    <div class="contact">
      <h2>Contact Me</h2>
      <p>Email Id :<br>hello@brightgearlabs.com</p>
      <p>Website :<br>www.brightgearlabs.com</p>
    </div>
    <div class="lockup" style="left:478px;top:160px">
      <div class="lockup-row"><span class="lockup-dot"></span><span class="lockup-name" style="font-size:20px">Brightgear Labs</span></div>
    </div>
  </section>

  <section class="slide slide--thumb slide--features" style="left:653px;top:164px">
    <div class="rule" style="bottom:195px"></div>
    <div class="bar" style="top:34px;height:40px"></div>
    <div class="head"><p class="sub">Subtitle Here</p><h2 class="ttl">Paragraph Title</h2></div>
    <div class="mark"><span class="mark-dot"></span>Brightgear</div>
    <div class="fill fill--gears-warm" style="left:0;right:0;top:125px;bottom:0" role="img" aria-label="Orange band with faint gear drawing"></div>
    <div class="features features--light" style="top:142px">
      <div class="feature"><svg><use href="#icon-phone"/></svg><h3>Icon Text Here</h3><p>Lorem Ipsum is simply dummy text of the printing and typesetting industry. Lorem Ipsum has been the industry's standard dummy text ever since the 1500s, when an unknown printer took a galley of type and scrambled</p></div>
      <div class="feature"><svg><use href="#icon-team"/></svg><h3>Icon Text Here</h3><p>Lorem Ipsum is simply dummy text of the printing and typesetting industry. Lorem Ipsum has been the industry's standard dummy text ever since the 1500s, when an unknown printer took a galley of type and scrambled</p></div>
      <div class="feature"><svg><use href="#icon-chart"/></svg><h3>Icon Text Here</h3><p>Lorem Ipsum is simply dummy text of the printing and typesetting industry. Lorem Ipsum has been the industry's standard dummy text ever since the 1500s, when an unknown printer took a galley of type and scrambled</p></div>
    </div>
  </section>

  <section class="slide slide--thumb slide--project" style="left:653px;top:316px">
    <svg class="chart" width="592" height="320" aria-hidden="true">
      <rect width="592" height="320" fill="#6A4238"/>
      <polygon points="180,0 592,0 592,320 505,320" fill="#FFFFFF"/>
      <polygon points="525,0 592,0 592,67" fill="#E6753D"/>
    </svg>
    <div class="rule rule--light" style="left:56px"></div>
    <div class="bar" style="left:54px;top:206px;height:46px"></div>
    <h1 class="display" style="left:68px;top:208px;font-size:22px;line-height:24px">Project Title Here<br><span class="display-sub" style="font-size:16px">Subtitle Here</span></h1>
    <div class="lockup" style="left:480px;top:130px">
      <div class="lockup-row"><span class="lockup-dot"></span><span class="lockup-name" style="font-size:20px">Brightgear Labs</span></div>
    </div>
  </section>

  <section class="slide slide--thumb slide--brand-paragraph" style="left:653px;top:460px">
    <div class="lockup" style="left:135px;top:150px">
      <div class="lockup-row"><span class="lockup-dot"></span><span class="lockup-name" style="font-size:20px">Brightgear Labs</span></div>
    </div>
    <div class="rule" style="left:265px"></div>
    <div class="bar" style="left:263px;top:88px;height:40px"></div>
    <div class="head" style="left:276px;top:90px"><p class="sub">Subtitle Here</p><h2 class="ttl">Paragraph Title</h2></div>
    <div class="mark"><span class="mark-dot"></span>Brightgear</div>
    <div class="copy" style="position:absolute;left:276px;right:32px;top:134px;font-size:8.5px;line-height:13.5px">Lorem Ipsum is simply dummy text of the printing and typesetting industry. Lorem Ipsum has been the industry's standard dummy text ever since the 1500s, when an unknown printer took a galley of type and scrambled it to make a type specimen book. It has survived not only five centuries, but also the leap into electronic typesetting, remaining essentially unchanged. It was popularised in the 1960s with the release of Dryset sheets containing Lorem Ipsum passages.</div>
    <div class="footer">Copyright text here</div>
    <div class="page">01</div>
  </section>

  <section class="slide slide--thumb slide--photo-paragraph" style="left:653px;top:606px">
    <div class="fill fill--hand-gears" style="left:0;top:0;width:229px;bottom:18px" role="img" aria-label="Hand holding a cluster of metal gears"></div>
    <div class="rule" style="left:265px"></div>
    <div class="bar" style="left:263px;top:88px;height:40px"></div>
    <div class="head" style="left:276px;top:90px"><p class="sub">Subtitle Here</p><h2 class="ttl">Paragraph Title</h2></div>
    <div class="mark"><span class="mark-dot"></span>Brightgear</div>
    <div class="copy" style="position:absolute;left:276px;right:32px;top:134px;font-size:8.5px;line-height:13.5px">Lorem Ipsum is simply dummy text of the printing and typesetting industry. Lorem Ipsum has been the industry's standard dummy text ever since the 1500s, when an unknown printer took a galley of type and scrambled it to make a type specimen book. It has survived not only five centuries, but also the leap into electronic typesetting, remaining essentially unchanged. It was popularised in the 1960s with the release of Dryset sheets containing Lorem Ipsum passages.</div>
    <div class="footer">Copyright text here</div>
    <div class="page">01</div>
  </section>

  <section class="slide slide--thumb slide--photo-band" style="left:653px;top:762px">
    <div class="rule"></div>
    <div class="bar" style="top:88px;height:40px"></div>
    <div class="head" style="top:90px"><p class="sub">Subtitle Here</p><h2 class="ttl">Paragraph Title</h2></div>
    <div class="mark"><span class="mark-dot"></span>Brightgear</div>
    <div class="copy" style="position:absolute;left:218px;right:30px;top:74px;font-size:8px;line-height:13px">Lorem Ipsum is simply dummy text of the printing and typesetting industry. Lorem Ipsum has been the industry's standard dummy text ever since the 1500s, when an unknown printer took a galley of type and scrambled it to make a type specimen book. It has survived not only five centuries, but also the leap into electronic typesetting.</div>
    <div class="fill fill--gears-glow" style="left:218px;right:0;top:169px;bottom:18px" role="img" aria-label="Glowing gears and a hand adjusting a cog"></div>
    <div class="footer">Copyright text here</div>
    <div class="page">01</div>
  </section>

  <section class="slide slide--thumb slide--table" style="left:653px;top:908px">
    <div class="rule"></div>
    <div class="bar" style="top:18px;height:34px"></div>
    <div class="head" style="top:16px"><p class="sub">Subtitle Here</p><h2 class="ttl">Paragraph Title</h2></div>
    <table class="data-table">
      <thead><tr><th>SECTION</th><th>MAIN TITLE HERE</th></tr></thead>
      <tbody>
        <tr><td class="label">ICON - 1</td><td class="desc">Short sample note about this row of the table, describing one item in a few plain words.<br>A second line adds a little more detail for the reader here.</td></tr>
        <tr><td class="label">ICON - 1</td><td class="desc">Short sample note about this row of the table, describing one item in a few plain words.<br>A second line adds a little more detail for the reader here.</td></tr>
        <tr><td class="label">ICON - 1</td><td class="desc">Short sample note about this row of the table, describing one item in a few plain words.<br>A second line adds a little more detail for the reader here.</td></tr>
        <tr><td class="label">ICON - 1</td><td class="desc">Short sample note about this row of the table, describing one item in a few plain words.<br>A second line adds a little more detail for the reader here.</td></tr>
        <tr><td class="label">ICON - 1</td><td class="desc">Short sample note about this row of the table, describing one item in a few plain words.<br>A second line adds a little more detail for the reader here.</td></tr>
      </tbody>
    </table>
    <div class="footer">Copyright text here</div>
    <div class="page">01</div>
  </section>

  <section class="slide slide--thumb slide--graph-peaks" style="left:653px;top:1058px">
    <div class="rule"></div>
    <div class="bar" style="top:16px;height:34px"></div>
    <div class="head" style="top:16px"><p class="sub">Subtitle Here</p><h2 class="ttl">Graphs Title</h2></div>
    <svg class="chart" width="592" height="320" aria-hidden="true">
      <g>
        <path d="M18 280 Q65 270 73 222 Q81 270 128 280Z" fill="#D4834F"/>
        <path d="M88 280 Q140 265 148 175 Q156 265 208 280Z" fill="#E6753D"/>
        <path d="M160 280 Q215 262 223 128 Q231 262 286 280Z" fill="#C86B3A"/>
        <path d="M244 280 Q291 268 299 194 Q307 268 354 280Z" fill="#DE8A56"/>
        <path d="M316 280 Q366 264 374 147 Q382 264 432 280Z" fill="#E6753D"/>
        <path d="M399 280 Q441 270 449 222 Q457 270 499 280Z" fill="#D4834F"/>
        <path d="M474 280 Q516 270 524 222 Q532 270 574 280Z" fill="#E09463"/>
      </g>
      <line x1="18" y1="280" x2="574" y2="280" stroke="#C9B2A6" stroke-width="1.5"/>
      <g fill="#C8622E">
        <circle cx="73" cy="196" r="11"/><circle cx="148" cy="148" r="11"/><circle cx="223" cy="98" r="11" fill="#D4834F"/>
        <circle cx="299" cy="166" r="11" fill="#8A4A2E"/><circle cx="374" cy="119" r="11" fill="#A8603C"/>
        <circle cx="449" cy="196" r="11"/><circle cx="524" cy="196" r="11"/>
      </g>
    </svg>
  </section>

  <!-- ========== thumbnails, column B ========== -->
  <section class="slide slide--thumb slide--closing" style="left:919px;top:8px">
    <div class="panel-brown" style="width:400px"></div>
    <div class="rule rule--light" style="left:39px"></div>
    <div class="bar" style="left:37px;top:136px;height:48px"></div>
    <h1 class="display" style="left:52px;top:145px;font-size:25px">Thank you for your time</h1>
    <div class="lockup" style="left:496px;top:165px">
      <div class="lockup-row"><span class="lockup-dot"></span><span class="lockup-name" style="font-size:20px">Brightgear Labs</span></div>
    </div>
  </section>

  <section class="slide slide--thumb slide--divider" style="left:919px;top:164px">
    <div class="fill fill--blueprint" role="img" aria-label="Faint blueprint drawing of gears and machine parts"></div>
    <div class="rule rule--light" style="left:39px;bottom:108px"></div>
    <div class="bar bar--brown" style="left:37px;top:130px;height:62px"></div>
    <h1 class="display" style="left:53px;top:134px;font-size:24px">Sectione Divider Title Here<br><span class="display-sub">Subtitle Here</span></h1>
    <div class="mark mark--light"><span class="mark-dot"></span>Brightgear</div>
  </section>

  <section class="slide slide--thumb slide--paragraph" style="left:919px;top:316px">
    <div class="rule"></div>
    <div class="bar" style="top:34px;height:40px"></div>
    <div class="head"><p class="sub">Subtitle Here</p><h2 class="ttl">Paragraph Title</h2></div>
    <div class="mark"><span class="mark-dot"></span>Brightgear</div>
    <div class="copy" style="position:absolute;left:45px;width:518px;top:80px;font-size:8.5px;line-height:14px">
      <p>Lorem Ipsum is simply dummy text of the printing and typesetting industry. Lorem Ipsum has been the industry's standard dummy text ever since the 1500s, when an unknown printer took a galley of type and scrambled it to make a type specimen book. It has survived not only five centuries, but also the leap into electronic typesetting, remaining essentially unchanged. It was popularised in the 1960s with the release of Dryset sheets containing Lorem Ipsum passages, and more recently with desktop publishing software.</p>
      <p>Lorem Ipsum has been the industry's standard dummy text ever since the 1500s, when an unknown printer took a galley of type and scrambled it to make a type specimen book. It has survived not only five centuries, but also the leap into electronic typesetting.</p>
      <p>It was popularised in the 1960s with the release of Dryset sheets containing Lorem Ipsum passages, and more recently with desktop publishing software.</p>
    </div>
    <div class="footer">Copyright text here</div>
    <div class="page">01</div>
  </section>

  <section class="slide slide--thumb slide--two-column" style="left:919px;top:460px">
    <div class="rule"></div>
    <div class="bar" style="top:34px;height:40px"></div>
    <div class="head"><p class="sub">Subtitle Here</p><h2 class="ttl">Paragraph Title</h2></div>
    <div class="mark"><span class="mark-dot"></span>Brightgear</div>
    <div class="copy" style="position:absolute;left:45px;width:245px;top:80px;font-size:8.5px;line-height:14px">Lorem Ipsum is simply dummy text of the printing and typesetting industry. Lorem Ipsum has been the industry's standard dummy text ever since the 1500s, when an unknown printer took a galley of type and scrambled it to make a type specimen book. It has survived not only five centuries, but also the leap into electronic typesetting, remaining essentially unchanged. It was popularised in the 1960s with the release of Dryset sheets containing Lorem Ipsum passages.</div>
    <div class="copy" style="position:absolute;left:317px;width:245px;top:80px;font-size:8.5px;line-height:14px">Lorem Ipsum is simply dummy text of the printing and typesetting industry. Lorem Ipsum has been the industry's standard dummy text ever since the 1500s, when an unknown printer took a galley of type and scrambled it to make a type specimen book. It has survived not only five centuries, but also the leap into electronic typesetting, remaining essentially unchanged. It was popularised in the 1960s with the release of Dryset sheets containing Lorem Ipsum passages.</div>
    <div class="footer">Copyright text here</div>
    <div class="page">01</div>
  </section>

  <section class="slide slide--thumb slide--features" style="left:919px;top:606px">
    <div class="rule"></div>
    <div class="bar" style="top:34px;height:40px"></div>
    <div class="head"><p class="sub">Subtitle Here</p><h2 class="ttl">Paragraph Title</h2></div>
    <div class="mark"><span class="mark-dot"></span>Brightgear</div>
    <div class="features features--dark" style="top:112px">
      <div class="feature"><svg><use href="#icon-phone"/></svg><h3>Icon Text Here</h3><p>Lorem Ipsum is simply dummy text of the printing and typesetting industry. Lorem Ipsum has been the industry's standard dummy text ever since the 1500s, when an unknown printer took a galley of type and scrambled</p></div>
      <div class="feature"><svg><use href="#icon-team"/></svg><h3>Icon Text Here</h3><p>Lorem Ipsum is simply dummy text of the printing and typesetting industry. Lorem Ipsum has been the industry's standard dummy text ever since the 1500s, when an unknown printer took a galley of type and scrambled</p></div>
      <div class="feature"><svg><use href="#icon-chart"/></svg><h3>Icon Text Here</h3><p>Lorem Ipsum is simply dummy text of the printing and typesetting industry. Lorem Ipsum has been the industry's standard dummy text ever since the 1500s, when an unknown printer took a galley of type and scrambled</p></div>
    </div>
    <div class="footer">Copyright text here</div>
    <div class="page">01</div>
  </section>

  <section class="slide slide--thumb slide--panel-left" style="left:919px;top:762px">
    <div class="fill fill--gears-warm" style="inset:0" role="img" aria-label="Orange toned photo of interlocking gears"></div>
    <div class="fill" style="left:0;top:0;bottom:0;width:259px;background:var(--brown)"></div>
    <div class="rule rule--light"></div>
    <div class="bar" style="top:56px;height:36px"></div>
    <div class="head head--light" style="top:56px"><p class="sub">Subtitle Here</p><h2 class="ttl">Paragraph Title</h2></div>
    <div class="copy copy--light" style="position:absolute;left:44px;width:196px;top:100px;font-size:8.5px;line-height:13.5px">Lorem Ipsum is simply dummy text of the printing and typesetting industry. Lorem Ipsum has been the industry's standard dummy text ever since the 1500s, when an unknown printer took a galley of type and scrambled it to make a type specimen book. It has survived not only five centuries, but also the leap into electronic typesetting.</div>
    <div class="mark mark--light"><span class="mark-dot"></span>Brightgear</div>
    <div class="footer footer--clear">Copyright text here</div>
    <div class="page">01</div>
  </section>

  <section class="slide slide--thumb slide--box-right" style="left:919px;top:908px">
    <div class="fill fill--gears-warm" style="inset:0" role="img" aria-label="Orange toned photo of gears and circuitry"></div>
    <div class="fill" style="left:329px;top:2px;width:211px;height:214px;background:var(--brown);opacity:.92"></div>
    <div class="head head--light" style="left:341px;top:24px"><p class="sub">Subtitle Here</p><h2 class="ttl">Paragraph Title</h2></div>
    <div class="copy copy--light" style="position:absolute;left:341px;width:188px;top:64px;font-size:8.5px;line-height:13.5px">Lorem Ipsum is simply dummy text of the printing and typesetting industry. Lorem Ipsum has been the industry's standard dummy text ever since the 1500s, when an unknown printer took a galley of type and scrambled it to make a type specimen book. It has survived not only five centuries.</div>
    <div class="footer footer--clear">Copyright text here</div>
    <div class="page">01</div>
  </section>

  <section class="slide slide--thumb slide--graph-bars" style="left:919px;top:1058px">
    <div class="rule"></div>
    <div class="bar" style="top:16px;height:34px"></div>
    <div class="head" style="top:16px"><p class="sub">Subtitle Here</p><h2 class="ttl">Graphs Title</h2></div>
    <svg class="chart" width="592" height="320" aria-hidden="true">
      <g stroke="#E8D6CC" stroke-width="1.5">
        <line x1="73" y1="100" x2="73" y2="282"/><line x1="265" y1="100" x2="265" y2="282"/><line x1="444" y1="100" x2="444" y2="282"/>
      </g>
      <g>
        <rect x="76" y="259" width="30" height="23" fill="#E6753D"/>
        <rect x="106" y="231" width="30" height="51" fill="#A65A35"/>
        <rect x="136" y="203" width="30" height="79" fill="#D88A50"/>
        <rect x="166" y="175" width="30" height="107" fill="#E6753D"/>
        <rect x="268" y="269" width="30" height="13" fill="#A65A35"/>
        <rect x="298" y="250" width="30" height="32" fill="#E6753D"/>
        <rect x="328" y="241" width="30" height="41" fill="#6A4238"/>
        <rect x="358" y="222" width="30" height="60" fill="#D88A50"/>
        <rect x="447" y="100" width="30" height="182" fill="#E6753D"/>
        <rect x="477" y="184" width="30" height="98" fill="#6A4238"/>
        <rect x="507" y="156" width="30" height="126" fill="#A65A35"/>
        <rect x="537" y="222" width="30" height="60" fill="#D88A50"/>
      </g>
    </svg>
  </section>

</main>
</body>
</html>
```